K-DRAV Landing Page

We want to re-design our current home page on our website (www.korvadrax.com) to simplify it and reduce it down to the (3) main products / services we offer. There are too many options of where they can go and it seems to be confusing for them. Additionally, we sell a higher end software product and we want the site to appear very professional for when CFO's considering our software can be confident in its quality and the long established company that we are. Our products and services are all about optimizing manufacturing production for sheet metal stampers (primarily automotive and appliance). I am including a rough power point layout of what we are thinking along with flyers for our three main products. We want to maintain the look and feel of the sample marketing materials as much as possible but does not have to match exactly. We will be producing the video ourselves to add where the power point shows a video being. Please review our website for any additional information.

```html
<!DOCTYPE html>
<html lang="en">
<head>
<meta charset="utf-8">
<title>K-DRAV Solutions</title>
<link href="https://fonts.googleapis.com/css2?family=Bebas+Neue&family=Barlow:wght@400;500;600;800&display=swap" rel="stylesheet">
<style>
:root{
  --yellow:#fdc211;
  --navy:#0a0f1e;
  --navy-2:#101a33;
  --ink:#111111;
  --text:#222222;
  --muted:#666666;
  --white:#ffffff;
}
*{margin:0;padding:0;box-sizing:border-box}
html,body{width:1200px;height:2631px;overflow:hidden}
body{position:relative;background:var(--white);font-family:"Barlow",sans-serif;color:var(--text)}
.abs{position:absolute}
.brand{display:flex;align-items:center;gap:9px;font-family:"Barlow",sans-serif;font-weight:800;font-size:22px;letter-spacing:.5px;color:var(--navy);white-space:nowrap}
.brand-square{width:28px;height:28px;background:var(--yellow);flex:none}
.site-header{left:0;top:0;width:1200px;height:84px;background:var(--white)}
.site-header .brand{position:absolute;left:141px;top:27px}
.main-nav{position:absolute;right:142px;top:33px;display:flex;gap:24px;font-size:13px;color:#444;white-space:nowrap}
.main-nav .active{color:var(--yellow)}
.hero{left:0;top:84px;width:1200px;height:570px}
.hero-title{left:141px;top:212px;font-family:"Bebas Neue",sans-serif;font-weight:400;font-size:56px;line-height:52px;color:var(--white);white-space:nowrap}
.hero-sub{left:143px;top:324px;font-size:17px;font-weight:600;line-height:22px;color:var(--white)}
.btn{display:inline-block;background:var(--yellow);color:var(--ink);font-size:13px;font-weight:500;padding:0 11px;height:35px;line-height:35px;text-transform:uppercase;letter-spacing:.2px;white-space:nowrap}
.hero-graphic{left:585px;top:132px;width:475px;height:420px;border-radius:50%;background:radial-gradient(circle at 55% 60%,#2d6fc2 0%,#163a72 28%,#0c1b3a 60%,rgba(10,15,30,0) 72%)}
h2.section-title{font-family:"Bebas Neue",sans-serif;font-weight:400;color:var(--ink);font-size:34px;line-height:32px;white-space:nowrap}
.copy{font-size:14px;line-height:25.5px;color:var(--text)}
.copy.light{font-size:12px;line-height:23px;color:var(--muted);letter-spacing:.3px}
.guarantee{left:0;top:2055px;width:1200px;text-align:center}
.guarantee h2{font-family:"Bebas Neue",sans-serif;font-weight:400;font-size:60px;line-height:60px;color:var(--ink)}
.guarantee p{font-size:17px;font-weight:500;line-height:22px;margin-top:12px;color:var(--ink)}
.footer{left:0;top:2300px;width:1200px;height:331px}
.footer-brand{left:0;top:2425px;width:1200px;display:flex;justify-content:center}
.footer-brand .brand{color:var(--white);font-size:26px}
.contact-item{top:2490px;display:flex;gap:12px;color:#e8e8e8;font-size:12px;line-height:19px;white-space:nowrap}
.contact-item svg{flex:none}
.footer-rule{left:0;top:2578px;width:1200px;height:1px;background:#1f2740}
.copyright{left:143px;top:2597px;color:#ddd;font-size:12px}
.social{top:2592px;display:flex;gap:8px;right:142px}
.social span{width:27px;height:27px;border-radius:50%;background:var(--yellow);display:block}
</style>
</head>
<body>

<header class="abs site-header">
  <div class="brand"><span class="brand-square"></span>K-DRAV Solutions</div>
  <nav class="main-nav">
    <span class="active">About</span><span>How We Help</span><span>K-DRAV Software</span><span>Transfer Simulation Service</span><span>Business Case</span><span>Resources</span><span>Contact</span>
  </nav>
</header>

<svg class="abs hero" viewBox="0 0 1200 570" aria-hidden="true">
  <defs>
    <linearGradient id="heroBg" x1="0" y1="0" x2="0" y2="1">
      <stop offset="0" stop-color="#070b17"/>
      <stop offset="0.7" stop-color="#0b1430"/>
      <stop offset="1" stop-color="#102250"/>
    </linearGradient>
  </defs>
  <polygon points="0,0 1200,0 1200,466 600,536 0,466" fill="url(#heroBg)"/>
  <polygon points="0,466 600,536 1200,466 1200,472 600,566 0,472" fill="var(--yellow)"/>
</svg>
<div class="abs hero-graphic" role="img" aria-label="Glowing business icons floating above an open hand with a CFO's badge"></div>
<h1 class="abs hero-title">We Are K-DRAV Solutions<br>Provides Software</h1>
<p class="abs hero-sub">And Service For Transfer Press Simulation And<br>Optimization On New And Existing Tooling.</p>
<a class="abs btn" style="left:141px;top:389px">Contact Us Today</a>

<div class="abs" style="left:141px;top:746px;width:459px;height:282px;background:linear-gradient(120deg,#cfcac4 0%,#5a3d30 45%,#3b2a22 100%)" role="img" aria-label="Business team meeting around a laptop at a conference table, video preview"></div>
<svg class="abs" style="left:524px;top:954px" width="54" height="54" viewBox="0 0 54 54" aria-hidden="true">
  <circle cx="27" cy="27" r="24" fill="none" stroke="#fff" stroke-width="3"/>
  <polygon points="21,16 21,38 39,27" fill="#fff"/>
</svg>
<h2 class="abs section-title" style="left:665px;top:775px;font-size:40px;line-height:40px">Welcome to K-DRAV Solutions</h2>
<p class="abs copy light" style="left:665px;top:823px;width:400px">At our core, we are a software company committed to providing cuttingedge simulation and optimization solutions. However, we understand that our customers have diverse needs and requirements which may not fit with buying software at this time. That's why we offer flexible options for you to experience the power of K-DRAV.</p>
<a class="abs btn" style="left:665px;top:963px">Contact Us Today</a>

<h2 class="abs section-title" style="left:143px;top:1124px">New Tool Simulation and Optimization</h2>
<p class="abs copy" style="left:143px;top:1170px;width:420px">Are you starting a new transfer tooling program soon? Trust the experts at K-DRAV to make it the best one you've ever had! Know your production rates before you build and confidently launch your tooling at the HIGHEST possible production rates</p>
<a class="abs btn" style="left:141px;top:1294px;padding:0 15px">Request a Quote</a>
<div class="abs" style="left:600px;top:1105px;width:459px;height:247px;background:linear-gradient(160deg,#000 0%,#555 35%,#d4cc18 60%,#1c5fe0 80%,#000 100%)" role="img" aria-label="3D simulation render of a transfer press die set in blue and yellow"></div>

<div class="abs" style="left:141px;top:1420px;width:459px;height:247px;background:linear-gradient(160deg,#dfe9ee 0%,#b8c0c4 40%,#e6e23a 70%,#dfe9ee 100%)" role="img" aria-label="3D model of an existing progressive transfer tool on light background"></div>
<h2 class="abs section-title" style="left:648px;top:1428px">Existing Tool Optimization<br>(With or Without CAD)</h2>
<p class="abs copy" style="left:648px;top:1496px;width:415px">Are you at capacity in your transfer press, running your equipment harder than you'd like, or simply know you can be doing better? Our existing tool optimization service is a great way increase your production efficiency (OEE) and free up press capacity.</p>
<a class="abs btn" style="left:647px;top:1619px;padding:0 15px">Request a Quote</a>

<h2 class="abs section-title" style="left:141px;top:1754px">K-DRAV Software Products</h2>
<p class="abs copy" style="left:143px;top:1800px;width:400px">Without question, our most successful customers are the ones who use the software themselves. K-DRAV Users typically see as much as 40% increase in their production rates! Hard to believe? Try it and see for yourself!</p>
<a class="abs btn" style="left:141px;top:1924px;padding:0 15px">Request a Quote</a>
<div class="abs" style="left:600px;top:1735px;width:459px;height:247px;background:linear-gradient(165deg,#d8d8d8 0%,#7a7a7a 35%,#2e2e2e 70%,#f0f0f0 100%)" role="img" aria-label="Grayscale 3D render of transfer press tooling"></div>

<section class="abs guarantee">
  <h2>Our Guarantee</h2>
  <p>You'll make your money back in your first (5) projects or we'll<br>refund the entire purchase price!</p>
  <a class="btn" style="margin-top:26px">Contact Us Today</a>
</section>

<svg class="abs footer" viewBox="0 0 1200 331" aria-hidden="true">
  <polygon points="0,125 600,25 1200,125 1200,331 0,331" fill="var(--yellow)"/>
  <polygon points="0,128 600,48 1200,128 1200,331 0,331" fill="var(--navy)"/>
</svg>
<div class="abs footer-brand"><div class="brand"><span class="brand-square"></span>K-DRAV Solutions</div></div>

<div class="abs contact-item" style="left:141px">
  <svg width="34" height="34" viewBox="0 0 34 34" fill="none" stroke="#ddd" stroke-width="1.5"><path d="M17 31s-9-10-9-16a9 9 0 0 1 18 0c0 6-9 16-9 16z"/><circle cx="17" cy="15" r="3.5"/></svg>
  <div>PO Box 412. 88 Orrin Industrial Dr.<br>Calverton, MI 49000-0412</div>
</div>
<div class="abs contact-item" style="left:451px">
  <svg width="34" height="34" viewBox="0 0 34 34" fill="none" stroke="#ddd" stroke-width="1.5"><path d="M8 4l5 6-3 3c2 4 5 7 9 9l3-3 6 5-3 5C14 28 6 20 4 8z"/></svg>
  <div>PHONE<br>555-014-2270</div>
</div>
<div class="abs contact-item" style="left:652px">
  <svg width="34" height="34" viewBox="0 0 34 34" fill="none" stroke="#ddd" stroke-width="1.5"><rect x="4" y="12" width="26" height="18"/><rect x="9" y="4" width="16" height="10"/><path d="M9 18h4M16 18h4M23 18h3M9 23h4M16 23h4M23 23h3"/></svg>
  <div>FAX<br>555-014-2271</div>
</div>
<div class="abs contact-item" style="left:850px">
  <svg width="34" height="34" viewBox="0 0 34 34" fill="none" stroke="#ddd" stroke-width="1.5"><path d="M4 14l13-10 13 10v16H4z"/><path d="M4 14l13 9 13-9"/></svg>
  <div>EMAIL<br>info@korvadrax.com</div>
</div>

<div class="abs footer-rule"></div>
<p class="abs copyright">© 2024 K-DRAV SOLUTIONS. All Rights Reserved.</p>
<div class="abs social" aria-label="Social media links"><span></span><span></span><span></span><span></span></div>

</body>
</html>
```